Business Card for Fashion House

We need a business card design for our personalize fashion service for our customers. the business card should reflect reliability, luxury and creativity.
The brand Gravetto is extracted from "Graceful Vetto"; Gravetto provides fashion designs sprinkled with luxury and style tailored for our elite clients character profile.
Gravetto is created for those who embody class and elegance with a passion for style.
Target Market(s)
Affluent Customers
Industry/Entity Type
Fashion
Contact Information for Business Card
Rania Bou Khalil
Fashion Designer
Telephone: +971 5550123
Mobile +971 555987
Emal q@z.com
Website www.gravetto-example.com
Social Media Youtube g+ Facebook Instagram Pin /gravetto
Font styles to use
Other font styles liked:
- Audrey provided
Look and feel
Each slider illustrates characteristics of the customer's brand and the style your logo design should communicate.

```html
<!DOCTYPE html>
<html lang="en">
<head>
<meta charset="utf-8">
<title>Gravetto Business Card</title>
<link rel="stylesheet" href="https://fonts.googleapis.com/css2?family=Cormorant+Garamond:wght@400;500&family=Montserrat:wght@300;600&display=swap">
<style>
  :root {
    --backdrop: #cfcac6;
    --card: #2f2a29;
    --ink: #ecebea;
    --muted: #77716f;
    --shadow: rgba(0, 0, 0, 0.28);
  }
  * { box-sizing: border-box; margin: 0; padding: 0; }
  html, body {
    width: 1200px; height: 1000px; overflow: hidden;
    background: var(--backdrop);
  }
  .canvas { position: relative; width: 1200px; height: 1000px; }
  .card {
    position: absolute;
    width: 720px; height: 411px;
    background: var(--card);
    border-radius: 22px;
    box-shadow: 0 14px 30px var(--shadow);
    color: var(--ink);
  }
  .card-front { left: 110px; top: 55px; }
  .card-back { left: 370px; top: 530px; }

  /* Front */
  .brand-mark {
    position: absolute; left: 50%; top: 78px;
    width: 84px; height: 84px; margin-left: -42px;
    border: 3px solid var(--ink); border-radius: 50%;
  }
  .brand-name {
    position: absolute; left: 0; right: 0; top: 190px;
    text-align: center;
    font-family: "Cormorant Garamond", serif;
    font-weight: 400; font-size: 58px;
    letter-spacing: 0.42em; padding-left: 0.42em;
    color: var(--ink);
  }
  .brand-site {
    position: absolute; left: 0; right: 0; top: 300px;
    text-align: center;
    font-family: "Montserrat", sans-serif;
    font-weight: 300; font-size: 17px;
    color: var(--muted);
  }
  .brand-site strong { font-weight: 600; }

  /* Back */
  .person {
    position: absolute; right: 90px; top: 70px; text-align: left;
  }
  .person-name {
    font-family: "Montserrat", sans-serif;
    font-weight: 300; font-size: 22px; letter-spacing: 0.02em;
    text-transform: uppercase;
  }
  .person-role {
    font-family: "Cormorant Garamond", serif;
    font-size: 17px; margin-top: 2px;
  }
  .contact-list {
    position: absolute; left: 60px; top: 140px;
    list-style: none;
    font-family: "Cormorant Garamond", serif;
    font-size: 19px; letter-spacing: 0.08em;
  }
  .contact-list li {
    display: flex; align-items: center; gap: 12px;
    height: 30px;
  }
  .contact-list svg { width: 16px; height: 16px; flex: none; }
  .social-row {
    position: absolute; left: 60px; bottom: 80px;
    display: flex; align-items: center; gap: 16px;
  }
  .social-dot {
    width: 20px; height: 20px; border-radius: 50%;
    background: var(--ink);
  }
  .social-handle {
    font-family: "Cormorant Garamond", serif;
    font-size: 20px; letter-spacing: 0.06em;
  }
</style>
</head>
<body>
<main class="canvas">
  <section class="card card-front">
    <div class="brand-mark"></div>
    <h1 class="brand-name">GRAVETTO</h1>
    <p class="brand-site">www.<strong>gravetto-example</strong>.com</p>
  </section>

  <section class="card card-back">
    <div class="person">
      <h2 class="person-name">Rania Bou Khalil</h2>
      <p class="person-role">Fashion Designer</p>
    </div>

    <ul class="contact-list">
      <li>
        <svg viewBox="0 0 16 16" aria-hidden="true"><path d="M2 5c0-2 2-3 6-3s6 1 6 3l-3 1-1-2H6L5 6 2 5zM4 8h8l1 6H3l1-6z" fill="#ecebea"/></svg>
        +971 5550123
      </li>
      <li>
        <svg viewBox="0 0 16 16" aria-hidden="true"><rect x="4" y="1" width="8" height="14" rx="1.5" fill="none" stroke="#ecebea" stroke-width="1.5"/><circle cx="8" cy="12.5" r="0.9" fill="#ecebea"/></svg>
        +971 555987
      </li>
      <li>
        <svg viewBox="0 0 16 16" aria-hidden="true"><circle cx="8" cy="8" r="6.5" fill="none" stroke="#ecebea" stroke-width="1.4"/><path d="M1.5 8h13M8 1.5c-3 3.5-3 9.5 0 13M8 1.5c3 3.5 3 9.5 0 13" fill="none" stroke="#ecebea" stroke-width="1.2"/></svg>
        www.gravetto-example.com
      </li>
      <li>
        <svg viewBox="0 0 16 16" aria-hidden="true"><rect x="1.5" y="3.5" width="13" height="9" fill="none" stroke="#ecebea" stroke-width="1.4"/><path d="M1.5 3.5 8 9l6.5-5.5" fill="none" stroke="#ecebea" stroke-width="1.4"/></svg>
        q@z.com
      </li>
    </ul>

    <div class="social-row" aria-label="Social media channels">
      <span class="social-dot"></span>
      <span class="social-dot"></span>
      <span class="social-dot"></span>
      <span class="social-dot"></span>
      <span class="social-dot"></span>
      <span class="social-handle">/gravetto</span>
    </div>
  </section>
</main>
</body>
</html>
```